Upcoming Importing and Distribution Business Needs A Packaging Design!

We are an importing and distribution company that is importing reams of paper into New Zealand; now we have confirmed the product we need a design mocked up for the reams of paper!

We need packaging for the individual reams and then also the box that will hold 5 reams.

Each ream needs to have information on it, including:
A4 Size
500 sheets
80g/m2
Home and Office Use

(On the back of the product) Company contact information
Harcourt Traders Limited
PO Box 7264
Christchurch 8140
New Zealand
(Email) office@harcourttraders.example.nz.

It is being brought in by our company, Harcourt Traders (logo attached)

We can't have too many colours in the design as it drives the price up very quickly.

Target Market(s)

Businesses and people that use paper to print documents

Industry/Entity Type

Retail

Requirements
Must have
• Clear simplistic labelling, be eye catching and stand out.
Should not have
• Not too many colours, will drive the price up too much

```html
<!DOCTYPE html>
<html lang="en">
<head>
<meta charset="utf-8">
<title>Harcourt Traders – A4 Ream Packaging</title>
<link rel="stylesheet" href="https://fonts.googleapis.com/css2?family=Open+Sans:wght@400;600;800&family=Cinzel:wght@500&display=swap">
<style>
  :root {
    --backdrop: #b5d8fb;
    --paper: #ffffff;
    --ink: #2b2b2b;
    --black: #1a1a1a;
    --yellow: #f4b433;
    --red: #d9262c;
  }
  * { box-sizing: border-box; margin: 0; padding: 0; }
  html, body {
    width: 1200px;
    height: 900px;
    overflow: hidden;
    background: var(--backdrop);
    font-family: "Open Sans", Arial, sans-serif;
    color: var(--ink);
  }
  .packaging-net {
    position: absolute;
    top: 96px;
    left: 60px;
    display: flex;
    gap: 20px;
  }
  .panel {
    background: var(--paper);
    height: 707px;
    position: relative;
    overflow: hidden;
  }
  .panel--front { width: 500px; }
  .panel--spine { width: 70px; }
  .panel--back  { width: 500px; }
  .panel svg { display: block; width: 100%; height: 100%; }

  .stripe--yellow { stroke: var(--yellow); }
  .stripe--black  { stroke: var(--black); }
  .stripe--red    { stroke: var(--red); }

  .brand-mark { fill: none; stroke: var(--ink); stroke-width: 2; }
  .brand-name { font-family: "Open Sans", Arial, sans-serif; font-weight: 400; fill: var(--ink); }

  .usage-line   { font-family: "Open Sans", Arial, sans-serif; font-weight: 400; fill: var(--ink); font-size: 38px; }
  .size-mark    { font-family: "Cinzel", Georgia, serif; font-weight: 500; fill: var(--yellow); font-size: 140px; }
  .sheet-count  { font-family: "Open Sans", Arial, sans-serif; font-weight: 800; fill: var(--black); font-size: 26px; }
  .paper-weight { font-family: "Open Sans", Arial, sans-serif; font-weight: 800; fill: var(--red); font-size: 28px; }

  .spine-box  { fill: none; stroke: var(--red); stroke-width: 1.5; }
  .spine-text { font-family: "Open Sans", Arial, sans-serif; font-weight: 600; fill: var(--ink); font-size: 13px; }

  .back-brand {
    position: absolute;
    top: 34px;
    left: 34px;
    display: flex;
    align-items: center;
    gap: 12px;
  }
  .back-brand__mark {
    width: 40px;
    height: 40px;
    border: 2px solid var(--ink);
    border-radius: 50%;
  }
  .back-brand__name { font-size: 22px; font-weight: 400; color: var(--ink); }
  .contact-block {
    position: absolute;
    left: 0;
    right: 0;
    bottom: 56px;
    text-align: center;
    font-size: 16px;
    line-height: 1.45;
    font-weight: 600;
    font-style: normal;
    color: var(--ink);
  }
</style>
</head>
<body>
  <main class="packaging-net" aria-label="A4 ream wrapper, flat layout">

    <section class="panel panel--front" aria-label="Front face">
      <svg viewBox="0 0 500 707">
        <g class="corner-stripes" transform="translate(150,0) rotate(137)" stroke-width="4">
          <line class="stripe--yellow" x1="0" y1="0"  x2="230" y2="0"/>
          <line class="stripe--black"  x1="0" y1="6"  x2="230" y2="6"/>
          <line class="stripe--red"    x1="0" y1="12" x2="230" y2="12"/>
        </g>

        <g class="brand">
          <circle class="brand-mark" cx="262" cy="74" r="22"/>
          <text class="brand-name" x="296" y="83" font-size="24">Harcourt Traders</text>
        </g>

        <g class="diagonal-label" transform="translate(0,610) rotate(-35)">
          <line class="stripe--yellow" x1="-20" y1="0"  x2="720" y2="0"  stroke-width="4"/>
          <line class="stripe--black"  x1="-20" y1="6"  x2="720" y2="6"  stroke-width="4"/>
          <line class="stripe--red"    x1="-20" y1="12" x2="720" y2="12" stroke-width="4"/>
          <text class="usage-line" x="60" y="-16">Home and Office Use</text>
          <text class="size-mark" x="282" y="130">A4</text>
          <text class="sheet-count" x="300" y="70" text-anchor="end">500 sheets</text>
          <text class="paper-weight" x="290" y="104" text-anchor="end">80g/m2</text>
        </g>
      </svg>
    </section>

    <section class="panel panel--spine" aria-label="Side panel">
      <svg viewBox="0 0 70 707">
        <g transform="translate(35,110) rotate(90)">
          <rect class="spine-box" x="-60" y="-22" width="120" height="44"/>
          <text class="spine-text" x="0" y="-4" text-anchor="middle">80g/m2</text>
          <text class="spine-text" x="0" y="14" text-anchor="middle">500 x A4</text>
        </g>
        <g stroke-width="3">
          <line class="stripe--yellow" x1="26" y1="260" x2="26" y2="560"/>
          <line class="stripe--black"  x1="32" y1="260" x2="32" y2="560"/>
          <line class="stripe--red"    x1="38" y1="260" x2="38" y2="560"/>
        </g>
      </svg>
    </section>

    <section class="panel panel--back" aria-label="Back face">
      <div class="back-brand">
        <span class="back-brand__mark"></span>
        <span class="back-brand__name">Harcourt Traders</span>
      </div>
      <address class="contact-block">
        Harcourt Traders Limited<br>
        PO Box 7264<br>
        Christchurch 8140<br>
        New Zealand<br>
        office@harcourttraders.example.nz
      </address>
    </section>

  </main>
</body>
</html>
```